Powerpoint Presentation

We have a basic 8 page presentation that we would like created on powerpoint. The presentation is very simple dot points and we would like to jazz it up with relevant photos/images relating to the topic on each page.

The topic of the presentation is 'creating a powerful presence and knowing your personal brand' (see attached files).

Target Market(s)

Business women

Requirements
Must have
• Images that match the content on each page

```html
<!DOCTYPE html>
<html lang="en">
<head>
<meta charset="utf-8">
<title>About Open Stage</title>
<link href="https://fonts.googleapis.com/css2?family=Questrial&family=Open+Sans:wght@400;600&family=Roboto+Condensed:wght@700&display=swap" rel="stylesheet">
<style>
  :root {
    --orange: #f07a22;
    --ink: #3c3c3c;
    --body: #4a4a4a;
    --footer: #535858;
    --header-top: #ffffff;
    --header-bottom: #e6e6e6;
    --white: #ffffff;
  }
  * { margin: 0; padding: 0; box-sizing: border-box; }
  html, body { width: 1200px; height: 900px; overflow: hidden; background: var(--white); }
  .slide { position: relative; width: 1200px; height: 900px; overflow: hidden; background: var(--white); }

  .slide-header {
    position: absolute; left: 0; top: 0; width: 1200px; height: 100px;
    background: linear-gradient(to bottom, var(--header-top), var(--header-bottom));
  }
  .slide-title {
    position: absolute; left: 44px; top: 26px;
    font-family: "Questrial", sans-serif; font-weight: 400; font-size: 43px;
    color: var(--ink); letter-spacing: 0.5px;
  }
  .slide-title .accent { color: var(--orange); }
  .brand {
    position: absolute; right: 12px; top: 8px; text-align: right;
  }
  .brand-mark {
    display: block; width: 52px; height: 52px; background: var(--orange);
    margin-left: auto; margin-right: 130px; border-radius: 4px;
  }
  .brand-name {
    display: block; margin-top: 8px;
    font-family: "Questrial", sans-serif; font-size: 26px; color: var(--orange); line-height: 1;
  }

  .backdrop-texture {
    position: absolute; left: 640px; top: 100px; width: 560px; height: 740px;
    background: radial-gradient(ellipse at 85% 35%, rgba(225,225,225,0.55), rgba(255,255,255,0) 70%);
  }

  .content { position: absolute; left: 0; top: 0; width: 1200px; height: 840px; }
  .point-heading {
    position: absolute; left: 57px;
    display: flex; align-items: center;
    font-family: "Open Sans", sans-serif; font-size: 24.5px; color: var(--ink);
  }
  .point-heading .arrow-box {
    width: 36px; height: 36px; background: var(--orange); border-radius: 4px;
    display: flex; align-items: center; justify-content: center; margin-right: 25px;
  }
  .sub-point {
    position: absolute; left: 120px; width: 860px;
    font-family: "Open Sans", sans-serif; font-weight: 600; font-size: 17.5px;
    line-height: 28px; color: var(--body); padding-left: 24px;
  }
  .sub-point .chevron { position: absolute; left: 0; top: 7px; }

  .slide-footer {
    position: absolute; left: 0; top: 840px; width: 1200px; height: 60px;
    border-top: 7px solid var(--orange); background: var(--footer);
    display: flex; justify-content: space-between; align-items: center;
    padding: 0 40px 0 46px;
    font-family: "Roboto Condensed", sans-serif; font-weight: 700; font-size: 21px;
    color: var(--white); letter-spacing: 0.5px;
  }
</style>
</head>
<body>
<div class="slide">
  <header class="slide-header">
    <h1 class="slide-title">About <span class="accent">Open Stage</span></h1>
    <div class="brand">
      <span class="brand-mark"></span>
      <span class="brand-name">open stage studio</span>
    </div>
  </header>

  <div class="backdrop-texture" role="img" aria-label="Faint grey dot pattern fading across the right side"></div>

  <main class="content">
    <div class="point-heading" style="top:166px;">
      <span class="arrow-box"><svg width="20" height="16" viewBox="0 0 20 16"><path d="M2 8h14M10 2l6 6-6 6" fill="none" stroke="#fff" stroke-width="2.6" stroke-linecap="round" stroke-linejoin="round"/></svg></span>
      Lorem ipsum dolor sit ipsum Lorem ipsum dolor sit ipsum Lorem ipsum
    </div>
    <p class="sub-point" style="top:224px;"><svg class="chevron" width="11" height="14" viewBox="0 0 11 14"><path d="M1 0l10 7-10 7 3-7z" fill="#f07a22"/></svg>Lorem ipsum dolor sit ipsum Lorem ipsum dolor sit ipsum Lorem ipsum&nbsp; Lorem ipsum dolor sit ipsum Lorem ipsum dolor sit ipsum Lorem ipsum</p>
    <p class="sub-point" style="top:311px;"><svg class="chevron" width="11" height="14" viewBox="0 0 11 14"><path d="M1 0l10 7-10 7 3-7z" fill="#f07a22"/></svg>Lorem ipsum dolor sit ipsum Lorem ipsum dolor sit ipsum Lorem ipsum&nbsp; Lorem ipsum dolor sit ipsum Lorem ipsum dolor sit ipsum Lorem ipsum</p>
    <p class="sub-point" style="top:398px;"><svg class="chevron" width="11" height="14" viewBox="0 0 11 14"><path d="M1 0l10 7-10 7 3-7z" fill="#f07a22"/></svg>Lorem ipsum dolor sit ipsum Lorem ipsum dolor sit ipsum Lorem ipsum&nbsp; Lorem ipsum dolor sit ipsum Lorem ipsum dolor sit ipsum Lorem ipsum</p>

    <div class="point-heading" style="top:481px;">
      <span class="arrow-box"><svg width="20" height="16" viewBox="0 0 20 16"><path d="M2 8h14M10 2l6 6-6 6" fill="none" stroke="#fff" stroke-width="2.6" stroke-linecap="round" stroke-linejoin="round"/></svg></span>
      Lorem ipsum dolor sit ipsum Lorem ipsum dolor sit ipsum Lorem ipsum
    </div>
    <p class="sub-point" style="top:539px;"><svg class="chevron" width="11" height="14" viewBox="0 0 11 14"><path d="M1 0l10 7-10 7 3-7z" fill="#f07a22"/></svg>Lorem ipsum dolor sit ipsum Lorem ipsum dolor sit ipsum Lorem ipsum&nbsp; Lorem ipsum dolor sit ipsum Lorem ipsum dolor sit ipsum Lorem ipsum</p>
    <p class="sub-point" style="top:626px;"><svg class="chevron" width="11" height="14" viewBox="0 0 11 14"><path d="M1 0l10 7-10 7 3-7z" fill="#f07a22"/></svg>Lorem ipsum dolor sit ipsum Lorem ipsum dolor sit ipsum Lorem ipsum&nbsp; Lorem ipsum dolor sit ipsum Lorem ipsum dolor sit ipsum Lorem ipsum</p>
    <p class="sub-point" style="top:713px;"><svg class="chevron" width="11" height="14" viewBox="0 0 11 14"><path d="M1 0l10 7-10 7 3-7z" fill="#f07a22"/></svg>Lorem ipsum dolor sit ipsum Lorem ipsum dolor sit ipsum Lorem ipsum&nbsp; Lorem ipsum dolor sit ipsum Lorem ipsum dolor sit ipsum Lorem ipsum</p>
  </main>

  <footer class="slide-footer">
    <span class="page-number">Page No. 00</span>
    <span class="copyright">Copyright@2013</span>
  </footer>
</div>
</body>
</html>
```